Fundbolt Informational Banners for Ember Hollow Drift

Hello, We are currently in the Process of doing a Fundbolt Campaign which is due on the 4th. We need a Grungy/Dirty Dark Dead Feeling set of Banners, and Informational Pieces in Various Sizes.
Banner Sizes:
640px × 88px Normall Banner
640px × 57px Breaker Banner
700px × 93px Header Banner
640px × 635px Display Box for Rewards
A Larger box, that needs to have a Seamless beginning and ending also needs to be made, so it can be extended as more text and so-forth is completed.

We are looking for very Dead, Dark looking images, thesr are ment to be displayed on the fundbolt webpage they need to flow well with the fundbolt form, as well as show off our things, simple or advanced. They need to match our style.

NOTE IMPORTANT!!!!
THESE ARE NOT ADVERTISING BANNERS, THESE ARE BANNERS FOR THE FUNDBOLT WEBSITE FOR A CAMPAIGN PLEASE DO SOME HOMEWORK BEFORE ATTEMPTING THESE IMAGES WE ARE NOT LOOKING FOR ADVERTISING BANNERS WE ARE LOOKING FOR INFORMATIONAL PIECES

Example of words that will be used on the various Banners

"Physical Add-ons"
"Digital Add-ons"
"Who we are"
"What is Ember Hollow Drift?"
"What is Procedural Generation?"
"Why are you Attempting this?"

THESE ARE EXAMPLE SENTENCES THAT WILL BE IN THE BANNERS I REPEAT THESE ARE NOT ADVERTISING WEBBANNERS
Updates

Everyone is Doing wonderful, thank you all for making such lovely work. thank You. Keep it up, remember undead feel, it must be functional piece on the fundbolt website. :3 

Target Market(s)

Zombie, and Undead ages People 13-51 that are Gamers

Industry/Entity Type

Digital

Requirements
Must have
• These Designs must be Boxes and Banners, and Break Points for a Fundbolt Information Display I will provide a few links here.
http://www.fundbolt.example/projects/quarvex/lament-shores-of-veldrith
http://www.fundbolt.example/projects/brindlework/venture-solace

Our Artwork Style & Concept Artwork can be found here
http://www.gamevault-plaza.example/games/ember-hollow-drift/images

```html
<!DOCTYPE html>
<html lang="en">
<head>
<meta charset="utf-8">
<title>Digital Add-ons — Section Banner</title>
<link rel="stylesheet" href="https://fonts.googleapis.com/css2?family=Open+Sans:wght@400&display=swap">
<style>
  :root {
    --ink-black: #050504;
    --moss-dark: #14170f;
    --moss-mid: #232619;
    --blood: #c3141b;
    --blood-deep: #6a0708;
    --ember: #ff2a2a;
    --title-red: #e8262c;
  }
  html, body {
    margin: 0;
    padding: 0;
    width: 1200px;
    height: 165px;
    overflow: hidden;
    background: var(--ink-black);
  }
  .section-banner {
    position: relative;
    width: 1200px;
    height: 165px;
    overflow: hidden;
    background: var(--ink-black);
  }
  .banner-backdrop {
    position: absolute;
    inset: 0;
    background:
      radial-gradient(ellipse 90px 120px at 20px 60px, rgba(195,20,27,0.85), transparent 75%),
      radial-gradient(ellipse 140px 70px at 290px 30px, rgba(195,20,27,0.55), transparent 75%),
      radial-gradient(ellipse 60px 50px at 230px 150px, rgba(150,14,16,0.5), transparent 75%),
      radial-gradient(ellipse 200px 90px at 560px 70px, rgba(35,38,25,0.9), transparent 80%),
      radial-gradient(ellipse 120px 80px at 820px 40px, rgba(106,7,8,0.45), transparent 80%),
      linear-gradient(90deg, var(--blood-deep) 0%, var(--moss-dark) 18%, var(--moss-mid) 45%, var(--moss-dark) 70%, var(--ink-black) 85%);
  }
  .creature-artwork {
    position: absolute;
    right: 0;
    top: 0;
    width: 230px;
    height: 165px;
    background:
      radial-gradient(ellipse 60px 120px at 210px 90px, rgba(255,42,42,0.85), transparent 80%),
      radial-gradient(ellipse 70px 60px at 110px 70px, rgba(70,60,45,0.7), transparent 80%),
      radial-gradient(ellipse 90px 40px at 150px 150px, rgba(195,20,27,0.7), transparent 80%),
      linear-gradient(90deg, transparent 0%, rgba(40,10,8,0.6) 40%, rgba(120,12,14,0.6) 100%);
  }
  .banner-title {
    position: absolute;
    left: 114px;
    top: 58px;
    margin: 0;
    font-family: "Open Sans", sans-serif;
    font-weight: 400;
    font-size: 45px;
    line-height: 1;
    letter-spacing: -0.5px;
    color: var(--title-red);
  }
</style>
</head>
<body>
  <header class="section-banner">
    <div class="banner-backdrop" role="img" aria-label="Dark grungy texture with blood-red glows"></div>
    <div class="creature-artwork" role="img" aria-label="Undead creature artwork lit in red"></div>
    <h1 class="banner-title">Digital Add-ons</h1>
  </header>
</body>
</html>
```